Real Estate Investment Company Needs A Business Card Designed

I need a business card designed for my use. We are a real estate investment company based in Omaha, Nebraska that specializes in buying, rehabbing and selling single family and multifamily properties. Would love designs that incorporate our logo and colors

Industry/Entity Type

Business

Contact Information for Business Card

Marlow Pettigrew | President & CEO
4837 North 52nd Avenue, Ste 200
Omaha, NE 68214
(402) 555-7428
marlow@quillfenhomes.example
www.QuillfenHomes.example

Font styles to use
Serif

Colors
0255a3
3276b5

Requirements
Must have
• Our logo

```html
<!DOCTYPE html>
<html lang="en">
<head>
<meta charset="utf-8">
<title>Quillfen Homes – Business Card</title>
<link href="https://fonts.googleapis.com/css2?family=Source+Sans+3:wght@400;600;700&display=swap" rel="stylesheet">
<style>
  :root {
    --backdrop: #e3e3e3;
    --card-dark: #0d0e10;
    --card-dark-edge: #1c1e22;
    --card-light: #ffffff;
    --brand-blue: #0255a3;
    --brand-blue-light: #3276b5;
    --accent-blue: #1d6fd0;
    --text-light: #f2f2f2;
    --text-muted: #c9ccd1;
    --divider: #7a7d82;
  }
  * { box-sizing: border-box; margin: 0; padding: 0; }
  html, body {
    width: 1200px; height: 900px; overflow: hidden;
    background: var(--backdrop);
    font-family: "Source Sans 3", "Myriad Pro", Arial, sans-serif;
  }
  .canvas {
    position: relative; width: 1200px; height: 900px;
    display: flex; align-items: center; justify-content: center; gap: 44px;
  }
  .card {
    width: 540px; height: 310px; border-radius: 22px; overflow: hidden;
    position: relative;
    box-shadow: 0 14px 30px rgba(0,0,0,0.22);
  }
  /* Front */
  .card--front {
    background: radial-gradient(ellipse at 50% 45%, var(--card-dark-edge) 0%, var(--card-dark) 70%);
    display: flex; align-items: center; justify-content: center;
  }
  .wordmark {
    display: flex; align-items: center; gap: 12px;
    font-weight: 700; letter-spacing: 0.04em; color: var(--accent-blue);
    text-transform: uppercase; white-space: nowrap;
  }
  .wordmark__dot {
    width: 26px; height: 26px; border-radius: 50%; background: var(--accent-blue);
  }
  .card--front .wordmark { font-size: 34px; }
  /* Back */
  .card--back { background: var(--card-light); }
  .back__top {
    height: 150px; display: flex; align-items: center; justify-content: center;
  }
  .card--back .wordmark { font-size: 30px; color: var(--brand-blue); }
  .card--back .wordmark__dot { background: var(--brand-blue); width: 22px; height: 22px; }
  .back__rule {
    height: 7px;
    background: linear-gradient(90deg, var(--brand-blue), var(--brand-blue-light));
    border-bottom: 1px solid #5b8fcf;
  }
  .back__bottom {
    height: 153px;
    background: linear-gradient(180deg, #16181c 0%, var(--card-dark) 100%);
    display: flex; align-items: center; padding: 0 24px 0 0;
  }
  .identity {
    width: 248px; text-align: right; padding-right: 16px;
  }
  .identity__name { color: var(--accent-blue); font-size: 21px; font-weight: 600; }
  .identity__title { color: var(--text-muted); font-size: 16px; margin-top: 4px; }
  .back__divider { width: 1px; height: 108px; background: var(--divider); }
  .contact { list-style: none; padding-left: 14px; }
  .contact__item {
    display: flex; align-items: flex-start; gap: 8px;
    color: var(--text-light); font-size: 13.5px; line-height: 19px;
  }
  .contact__icon { width: 15px; height: 15px; margin-top: 2px; flex: none; }
  .contact__item--indent { padding-left: 23px; }
</style>
</head>
<body>
<main class="canvas">
  <section class="card card--front" aria-label="Card front">
    <div class="wordmark"><span class="wordmark__dot"></span>Quillfen Homes</div>
  </section>

  <section class="card card--back" aria-label="Card back">
    <div class="back__top">
      <div class="wordmark"><span class="wordmark__dot"></span>Quillfen Homes</div>
    </div>
    <div class="back__rule"></div>
    <div class="back__bottom">
      <div class="identity">
        <p class="identity__name">Marlow Pettigrew</p>
        <p class="identity__title">President &amp; CEO</p>
      </div>
      <div class="back__divider"></div>
      <ul class="contact">
        <li class="contact__item">
          <svg class="contact__icon" viewBox="0 0 16 16" aria-hidden="true"><path fill="#3276b5" d="M3.5 1.5l2.6 2.8-1.4 2a9 9 0 0 0 5 5l2-1.4 2.8 2.6-1.6 2C7.5 14.5 1.5 8.5 1.5 3.1z"/></svg>
          (402) 555-7428
        </li>
        <li class="contact__item">
          <svg class="contact__icon" viewBox="0 0 16 16" aria-hidden="true"><rect x="1.5" y="3.5" width="13" height="9" rx="1" fill="none" stroke="#3276b5" stroke-width="1.6"/><path d="M1.8 4l6.2 5 6.2-5" fill="none" stroke="#3276b5" stroke-width="1.6"/></svg>
          marlow@quillfenhomes.example
        </li>
        <li class="contact__item">
          <svg class="contact__icon" viewBox="0 0 16 16" aria-hidden="true"><circle cx="8" cy="8" r="6.3" fill="none" stroke="#3276b5" stroke-width="1.5"/><ellipse cx="8" cy="8" rx="2.8" ry="6.3" fill="none" stroke="#3276b5" stroke-width="1.2"/><path d="M1.8 8h12.4" stroke="#3276b5" stroke-width="1.2"/></svg>
          www.QuillfenHomes.example
        </li>
        <li class="contact__item">
          <svg class="contact__icon" viewBox="0 0 16 16" aria-hidden="true"><path fill="#3276b5" d="M8 1.5l7 6.2h-2.2V14.5H9.6V10.5H6.4v4H3.2V7.7H1z"/></svg>
          4837 North 52nd Avenue, Ste 200
        </li>
        <li class="contact__item contact__item--indent">Omaha, NE 68214</li>
      </ul>
    </div>
  </section>
</main>
</body>
</html>
```